Gratulation zur Firmengründung
Zielgruppe
Wir sind eine Steuerberatungskanzlei. Das Design soll potentiellen Neukunden gefallen!
Aufgabenstellung
Wir möchten einen Flyer im Format 21x9,8 erstellen. Eine Skizzierung der Idee findet sich in der angefügten Datei.

```html
<!DOCTYPE html>
<html lang="de">
<head>
<meta charset="utf-8">
<title>finanzlotsen.de – Flyer Firmengründung</title>
<link href="https://fonts.googleapis.com/css2?family=Arimo:ital,wght@0,400;0,700;1,400&display=swap" rel="stylesheet">
<style>
  :root {
    --green: #6fa52b;
    --grey-band: #6b6b6b;
    --paper: #fbfcf8;
    --stage: #e9e9e7;
    --ink: #1e1e1e;
    --white: #ffffff;
  }
  * { box-sizing: border-box; margin: 0; padding: 0; }
  html, body { width: 1200px; height: 1200px; overflow: hidden; }
  body {
    background: var(--stage);
    font-family: "Arimo", Arial, sans-serif;
    color: var(--ink);
    position: relative;
  }
  .flyer {
    position: absolute;
    left: 80px;
    width: 1040px;
    height: 485px;
    background: var(--paper);
    box-shadow: 0 6px 18px rgba(0,0,0,.18);
    overflow: hidden;
  }
  .flyer--front { top: 60px; }
  .flyer--back  { top: 620px; }

  /* Front */
  .front-photo {
    position: absolute;
    left: 245px; top: 0;
    width: 795px; height: 461px;
    background: linear-gradient(160deg, #c9c9c6 0%, #8f8f8d 55%, #767674 100%);
  }
  .front-headline {
    position: absolute;
    left: 0; top: 38px;
    padding: 10px 16px 12px 20px;
    background: var(--green);
    color: var(--white);
    font-size: 30px;
    font-weight: 400;
    line-height: 1.22;
  }
  .front-url {
    position: absolute;
    left: 48px; top: 418px;
    color: var(--green);
    font-size: 19px;
  }
  .front-band {
    position: absolute;
    left: 0; bottom: 0;
    width: 100%; height: 24px;
    background: var(--grey-band);
  }

  /* Back */
  .back-headline {
    position: absolute;
    left: 0; top: 70px;
    width: 520px; height: 50px;
    padding: 10px 0 0 22px;
    background: var(--green);
    color: var(--white);
    font-size: 29px;
    font-weight: 400;
    z-index: 2;
  }
  .photo {
    position: absolute;
    top: 105px; height: 250px;
  }
  .photo--family {
    left: 16px; width: 396px;
    background: linear-gradient(135deg, #e6e6e3 0%, #bdbdba 100%);
  }
  .photo--advisor {
    left: 420px; width: 272px;
    background: linear-gradient(135deg, #b5b5b2 0%, #e8e8e5 100%);
  }
  .info {
    position: absolute;
    left: 706px; top: 30px;
    width: 318px;
  }
  .info-title {
    font-style: italic;
    font-weight: 400;
    font-size: 19px;
    padding: 4px 0 3px 4px;
    border-top: 2px dotted var(--green);
    border-bottom: 2px dotted var(--green);
  }
  .info-text {
    margin-top: 6px;
    font-size: 12.6px;
    line-height: 1.36;
  }
  .info-text em { font-style: normal; color: var(--green); }
  .back-footer {
    position: absolute;
    left: 0; bottom: 0;
    width: 100%; height: 130px;
    background: var(--grey-band);
    color: var(--white);
  }
  .contact {
    position: absolute;
    left: 34px; top: 30px;
    font-size: 19px;
    font-style: normal;
    line-height: 1.3;
  }
  .contact .brand { color: var(--green); }
  .logo {
    position: absolute;
    right: 40px; top: 16px;
    width: 300px;
  }
  .logo-name {
    font-size: 40px;
    color: var(--ink);
    padding-bottom: 4px;
    border-bottom: 2px dotted var(--white);
  }
  .logo-sub {
    font-size: 14px;
    letter-spacing: .6px;
    white-space: nowrap;
    padding: 6px 0 5px;
    border-bottom: 2px dotted var(--white);
  }
</style>
</head>
<body>

<section class="flyer flyer--front" aria-label="Flyer Vorderseite">
  <div class="front-photo" role="img" aria-label="Foto: Geschäftsmann schneidet ein grünes Band zur Eröffnung durch"></div>
  <h1 class="front-headline">Wir gratulieren<br>zur Firmengründung!</h1>
  <p class="front-url">finanzlotsen.de</p>
  <div class="front-band"></div>
</section>

<section class="flyer flyer--back" aria-label="Flyer Rückseite">
  <h2 class="back-headline">Haben Sie steuerliche Fragen?</h2>
  <div class="photo photo--family" role="img" aria-label="Foto: Familie mit Kindern am Laptop"></div>
  <div class="photo photo--advisor" role="img" aria-label="Foto: Berater im Anzug mit Laptop in heller Halle"></div>

  <article class="info">
    <h3 class="info-title">Beratung für Existenzgründer</h3>
    <p class="info-text">Als kompetenter Partner in Steuer- und Unternehmensfragen begleiten wir Existenzgründer von Anfang an auf Ihrem Weg zu einem erfolgreichen Unternehmen. In einem strukturierten Prozess analysieren wir gemeinsam mit Ihnen Ihr Gründungsvorhaben und zeigen Ihnen Chancen, Problemfelder und Lösungen. Dabei haben wir stets den Erfolg Ihres <em>Gründungsvorhabens</em> vor Augen und bieten Ihnen neben wertvollen Tipps und unserer Erfahrung aus den unterschiedlichen Branchen Eines: Die Gewissheit, steuerlich alles richtig zu machen und nicht alleine mit Ihren Fragen zu sein. Konzentrieren Sie sich auf Ihre eigentliche Aufgabe als Existenzgründer: den Aufbau Ihres Unternehmens.</p>
  </article>

  <footer class="back-footer">
    <address class="contact">
      <span class="brand">finanzlotsen.de</span> Steuerberatungsgesellschaft mbH<br>
      Lindenallee 14 20144 Hamburg<br>
      T: 040/123 456 780 E: hamburg@finanzlotsen.de
    </address>
    <div class="logo">
      <div class="logo-name">finanzlotsen.de</div>
      <div class="logo-sub">STEUERBERATUNGSGESELLSCHAFT MBH</div>
    </div>
  </footer>
</section>

</body>
</html>
```